Beer Sommelier Business Card

Dear Designers,
I'm looking forward a Beer Sommelier business card. I'm a Beer Sommelier and also a Chef in Rio de Janeiro, Brazil but this card has to be a Beer Sommelier card.
I do consulting, brigade training, tastings and harmonizations.
Forget about themes such as rock and roll, motorcycles, conventional English pubs and bellied beer drinkers. This business card will be delivered to restaurant owners and investors in Rio.
It has to seek elegance rather than luxury, and refinement rather than fashion.
I work using a black dress shirt, a Varnel Osterby watch and a 18k 1981 Dumelle aviator eyeglasses. I'm a business man and It's all part of the game.
Obviously, it has to be written in PORTUGUESE (only) and just as little as possible.

Informations to be included:

Tiago Varquim

Beer Sommelier
Chef de Cuisine

Consultoria
Treinamento de Brigada
Degustações
Harmonizações

telephone number (just numbers): 947261380

email (just the adress): tiagovarquim@mailnest.example

PS:
The letter "c" on both words "Degustações" and "Harmonizações" they have a small trace under it.
The letter "o" on both words "Degustações" and "Harmonizações" they have a small wave above it.

Blame the Latin.

Best Regards

Target Market(s)

Restaurant Owners and Investors. I have to impress them with my business card before I offer my services.

Industry/Entity Type

Restaurant

Contact Information for Business Card

An unique and well constructed Sommelier Business Card

Requirements
Must have
• A firts look impact. An unique and well made design. Not an ordinary product.
• Tiago Varquim
• Beer Sommelier/Chef de Cuisine
• Consultoria
• Treinamento de Brigada
• Degustações
• Harmonizações
• telephone number (just numbers): 947261380
• email (just the adress): tiagovarquim@mailnest.example
• PS:
• The letter "c" on both words "Degustações" and "Harmonizações" they have a small trace under it.
• The letter "o" on both words "Degustações" and "Harmonizações" they have a small wave above it.
Nice to have
• Elegance, Refinement.
• Should be a Pro Style good Looking card,
• Forget themes like beer, chef and cuisine,
• It could be a laser engraved, metal, stainless steel, PVC, Triplex, Smooth, Letterpress, all black or any other good idea.
Should not have
• Words like telephone, email, cartoon pics or glass pics.
• Should not be an ordinary card that I could download from the web or use a web program and easily make by my self.
• Just Portuguese words

```html
<!DOCTYPE html>
<html lang="pt-BR">
<head>
<meta charset="utf-8">
<title>Tiago Varquim — Beer Sommelier</title>
<link rel="stylesheet" href="https://fonts.googleapis.com/css2?family=Tinos:wght@400;700&display=swap">
<style>
  :root {
    --ink: #1f1f1f;
    --band: #262626;
    --paper: #ffffff;
    --gold: #b8955a;
    --gold-light: #d9bf86;
    --stage: #d9d9d9;
  }
  * { margin: 0; padding: 0; box-sizing: border-box; }
  html, body { width: 1200px; height: 900px; overflow: hidden; }
  body {
    background: var(--stage);
    font-family: "Tinos", "Times New Roman", serif;
    position: relative;
  }
  .card {
    position: absolute;
    left: 240px;
    width: 720px;
    height: 400px;
    background: var(--paper);
    box-shadow: 0 6px 18px rgba(0,0,0,0.25);
    overflow: hidden;
  }
  .card--front { top: 40px; }
  .card--back { top: 460px; }

  .band {
    position: absolute;
    left: 0;
    width: 100%;
    background: var(--band);
  }
  .band--top { top: 0; height: 34px; border-bottom: 2px solid var(--gold-light); }
  .band--contact {
    top: 266px; height: 76px;
    border-top: 2px solid var(--gold-light);
    border-bottom: 2px solid var(--gold-light);
    display: flex; align-items: center;
    padding: 0 40px;
    color: var(--gold-light);
  }
  .band--bottom { bottom: 0; height: 50px; border-top: 2px solid var(--gold-light); }

  .wordmark {
    position: absolute;
    left: 0; width: 100%;
    text-align: center;
    color: var(--gold);
    font-weight: 400;
    font-size: 44px;
    letter-spacing: 1px;
  }
  .card--front .wordmark { top: 92px; }
  .card--back .wordmark { top: 96px; }

  .title {
    position: absolute;
    left: 0; width: 100%;
    text-align: center;
    color: var(--ink);
    font-weight: 700;
    font-size: 34px;
    line-height: 1;
  }
  .subtitle {
    position: absolute;
    left: 0; width: 100%;
    text-align: center;
    color: var(--gold);
    font-weight: 700;
    font-size: 24px;
    line-height: 1;
  }
  .card--front .title { top: 180px; }
  .card--front .subtitle { top: 218px; }
  .card--back .title { top: 190px; }
  .card--back .subtitle { top: 228px; }

  .name {
    font-size: 24px;
    letter-spacing: 1px;
    text-transform: uppercase;
    margin-right: auto;
  }
  .contact {
    display: flex; align-items: center; gap: 8px;
    font-size: 14px;
    margin-left: 44px;
  }
  .contact svg { width: 18px; height: 18px; flex: none; }

  .services {
    position: absolute;
    left: 0; width: 100%;
    top: 286px;
    text-align: center;
    color: #000;
    font-weight: 700;
    font-size: 22px;
  }
</style>
</head>
<body>

<section class="card card--front">
  <div class="band band--top"></div>
  <div class="wordmark">Tiago Varquim</div>
  <div class="title">Beer Sommelier</div>
  <div class="subtitle">Chef de Cuisine</div>
  <div class="band band--contact">
    <span class="name">Tiago Varquim</span>
    <span class="contact">
      <svg viewBox="0 0 18 18" aria-hidden="true">
        <circle cx="9" cy="9" r="8" fill="none" stroke="currentColor" stroke-width="1"/>
        <rect x="6.2" y="4.5" width="5.6" height="9" rx="1" fill="none" stroke="currentColor" stroke-width="1"/>
        <line x1="8.2" y1="12" x2="9.8" y2="12" stroke="currentColor" stroke-width="1"/>
      </svg>
      9 4726 1380
    </span>
    <span class="contact">
      <svg viewBox="0 0 18 18" aria-hidden="true">
        <circle cx="9" cy="9" r="8" fill="currentColor"/>
        <rect x="5" y="6" width="8" height="6" fill="none" stroke="#262626" stroke-width="1"/>
        <polyline points="5,6 9,9.5 13,6" fill="none" stroke="#262626" stroke-width="1"/>
      </svg>
      tiagovarquim@mailnest.example
    </span>
  </div>
</section>

<section class="card card--back">
  <div class="band band--top"></div>
  <div class="wordmark">Tiago Varquim</div>
  <div class="title">Beer Sommelier</div>
  <div class="subtitle">Chef de Cuisine</div>
  <div class="services">Consultoria - Degustações - Harmonizações - Treinamento de Brigada</div>
  <div class="band band--bottom"></div>
</section>

</body>
</html>
```